Kveldbrá - Start-up company selling electricity

Hello let me tell you about Kveldbrá.

Kveldbrá is start-up company selling electricity in Iceland. The operations of the company consist of making power usage forecasts for our customers, purchasing the electricity wholesale from the energy producers, and selling the electricity to the consumer. We are focused on tech by using optimization and machine learning to minimize electricity prices to our customers. Our marketing strategy is to portray a tech company mindset and to show dedication to driving down the electricity price on the market.

We need your help to make our website pop. Possible concepts to work with are as follows:

- Iceland the land of ice and fire
- Green energy
- Innovation
- Tech and data science

Link to our website: https://prufa.kveldbra.is/
We are open to ideas.
Thank you!

Target Market(s)

Electricity consumers both homes and companies.

Number of Pages Required

1 page

Font styles to use
Serif
Sans Serif

```html
<!DOCTYPE html>
<html lang="en">
<head>
<meta charset="utf-8">
<title>Kveldbrá – Same electricity, just cheaper</title>
<link href="https://fonts.googleapis.com/css2?family=Rubik:wght@400;500;700&display=swap" rel="stylesheet">
<style>
:root{
  --navy:#1b3563;
  --navy-deep:#142c57;
  --red:#a8302a;
  --ink:#222;
  --muted:#555;
  --white:#fff;
  --hero-a:#4a5f86;
  --hero-b:#6a7fa6;
}
*{box-sizing:border-box;margin:0;padding:0}
html,body{width:724px;height:1200px;overflow:hidden}
body{font-family:"Rubik",sans-serif;color:var(--ink);background:var(--white);position:relative}
.btn{position:absolute;background:var(--red);color:var(--white);font-weight:500;font-size:7.5px;text-transform:uppercase;display:flex;align-items:center;justify-content:center;border-radius:2px;letter-spacing:.2px}

/* header */
.site-header{position:absolute;left:0;top:0;width:724px;height:41px}
.brand{position:absolute;left:94px;top:14px;display:flex;align-items:center;gap:5px;font-family:"Rubik",sans-serif;font-weight:500;font-size:14px;color:var(--red);letter-spacing:.3px}
.brand-dot{width:11px;height:11px;border-radius:50%;background:var(--navy)}
.nav{position:absolute;left:338px;top:19px;display:flex;gap:10px;font-size:7.5px;color:var(--navy)}
.header-register{left:566px;top:12px;width:64px;height:21px}

/* hero */
.hero{position:absolute;left:0;top:41px;width:724px;height:256px;background:linear-gradient(100deg,var(--hero-a),var(--hero-b) 55%,#56698f)}
.hero-title{position:absolute;top:90px;width:100%;text-align:center;color:var(--white);font-weight:700;font-size:22px;letter-spacing:.2px}
.hero-text{position:absolute;top:126px;width:100%;text-align:center;color:var(--white);font-size:7.4px;line-height:12.6px}
.hero-more{left:329px;top:166px;width:66px;height:20px}
.dots{position:absolute;top:205px;left:349px;display:flex;gap:6px}
.dots span{width:5px;height:5px;border-radius:50%;border:1px solid var(--white)}
.dots span.on{background:var(--white)}

/* about */
.about-visual{position:absolute;left:88px;top:330px;width:200px;height:300px;border-radius:20px 20px 100px 100px;background:linear-gradient(165deg,#c99a86 0%,#9c7466 35%,#3c5a96 55%,#5a6a3a 85%,#8a8a2a)}
.about-mark{position:absolute;left:326px;top:336px;width:16px;height:16px;border-radius:50%;background:var(--navy)}
.about-label{position:absolute;left:324px;top:362px;font-size:7.5px;color:var(--red)}
.about-title{position:absolute;left:324px;top:377px;width:300px;font-weight:700;font-size:14px;line-height:21px;color:var(--ink)}
.about-copy{position:absolute;left:324px;top:428px;width:306px;font-size:7.3px;line-height:12.6px;color:var(--muted)}
.about-copy p+p{margin-top:12.6px}
.about-more{left:323px;top:589px;width:74px;height:20px}

/* future */
.future{position:absolute;left:0;top:660px;width:724px;height:257px;background:linear-gradient(90deg,#5d7299 0%,#6f83a8 45%,#8b97ad 75%,#6d7e9e)}
.future-title{position:absolute;left:97px;top:40px;color:var(--white);font-weight:700;font-size:14px}
.future-text{position:absolute;left:99px;top:67px;width:260px;color:var(--white);font-size:7.3px;line-height:11.6px}
.feature{position:absolute;top:119px;width:69px;height:74px;background:var(--white);border-radius:2px;display:flex;flex-direction:column;align-items:center;justify-content:flex-start;padding-top:8px;text-align:center;color:var(--navy);font-weight:500;font-size:7.3px;line-height:9.4px}
.feature svg{width:30px;height:30px;margin-bottom:5px}
.future-register{left:99px;top:210px;width:83px;height:22px}

/* prices */
.price-intro-title{position:absolute;left:97px;top:952px;font-weight:700;font-size:14px}
.price-intro-text{position:absolute;left:98px;top:982px;width:100px;font-size:7.3px;line-height:11.6px;color:var(--muted)}
.price-link{position:absolute;left:98px;top:1012px;font-size:7.4px;font-weight:500;color:var(--navy)}
.price-compare{left:99px;top:1031px;width:103px;height:22px}
.price-card{position:absolute;top:942px;width:182px;height:121px;color:var(--white);padding:15px 0 0 22px}
.price-card.navy{left:244px;background:var(--navy)}
.price-card.red{left:448px;background:var(--red)}
.price-name{font-weight:500;font-size:11px;line-height:11.5px}
.price-value{font-weight:700;font-size:30px;margin-top:9px;margin-left:-2px;letter-spacing:.5px}
.price-unit{font-size:8px;margin-top:2px;margin-left:2px}

/* footer */
.site-footer{position:absolute;left:0;top:1090px;width:724px;height:110px;background:var(--navy-deep);color:var(--white)}
.contact{position:absolute;top:28px;display:flex;gap:10px;align-items:flex-start}
.contact svg{width:20px;height:24px;flex:none}
.contact-label{font-weight:700;font-size:7.4px;text-transform:uppercase;margin-top:3px}
.contact-value{font-size:7.6px;margin-top:5px}
.divider{position:absolute;top:29px;width:1px;height:34px;background:#34507e}
.copyright{position:absolute;top:87px;width:100%;text-align:center;font-size:5px;color:#cfd6e4}
</style>
</head>
<body>

<header class="site-header">
  <div class="brand"><span class="brand-dot"></span>KVELDBRÁ</div>
  <nav class="nav"><span>Terms of business</span><span>Question &amp; Answer</span><span>About Kveldbrá</span></nav>
  <a class="btn header-register">Register</a>
</header>

<section class="hero" role="img" aria-label="Photo of technicians in hard hats servicing electrical equipment">
  <h1 class="hero-title">SAME ELECTRICITY - JUST CHEAPER!</h1>
  <p class="hero-text">Kveldbrá uses automation and artificial intelligence to achieve lower prices in the electricity market.<br>Our goal is to minimize the cost of energy sales, promote energy balance and offer good service.</p>
  <a class="btn hero-more">Read more</a>
  <div class="dots"><span></span><span class="on"></span><span></span></div>
</section>

<section class="about">
  <div class="about-visual" role="img" aria-label="Photo collage of an electrician at work and a lit house at dusk"></div>
  <div class="about-mark"></div>
  <p class="about-label">About Kveldbrá</p>
  <h2 class="about-title">What is Kveldbrá's unique position in the electricity sales market?</h2>
  <div class="about-copy">
    <p>Kveldbrá uses automation and artificial intelligence to achieve lower prices in the electricity market. Our goal is to minimize the cost of energy sales, promote energy balance and offer good service.</p>
    <p>Kveldbrá's goal is to offer its customers the most favorable electricity prices in Iceland. Electricity is part of the monthly costs of households and companies, and by doing business with Kveldbrá, savings can be achieved and operating costs reduced. Kveldbrá wants to make the electricity system "smarter". Data science and the use of artificial intelligence can maximize the efficiency of the electricity system, minimize electricity costs and promote energy balance. Therefore, it can be said that by trading with Kveldbrá, you support the development of the Icelandic electricity market.</p>
  </div>
  <a class="btn about-more">More details</a>
</section>

<section class="future" role="img" aria-label="Photo of a power substation with pylons and insulators">
  <h2 class="future-title">The Future is Exciting</h2>
  <p class="future-text">Let's make the electricity system smarter together. Kveldbrá uses artificial intelligence, data science and automation to minimize costs and promote eccentricity</p>
  <div class="feature" style="left:99px">
    <svg viewBox="0 0 30 30" fill="none" stroke="#1b3563" stroke-width="1.2"><rect x="8" y="6" width="14" height="16" rx="3"/><path d="M12 22v4M18 22v4M8 11H4M8 17H4M22 11h4M22 17h4"/><circle cx="15" cy="14" r="3"/></svg>
    Artificial<br>Intelligence
  </div>
  <div class="feature" style="left:186px">
    <svg viewBox="0 0 30 30" fill="none" stroke="#1b3563" stroke-width="1.2"><ellipse cx="15" cy="15" rx="13" ry="5"/><ellipse cx="15" cy="15" rx="13" ry="5" transform="rotate(60 15 15)"/><ellipse cx="15" cy="15" rx="13" ry="5" transform="rotate(-60 15 15)"/><circle cx="15" cy="15" r="3"/></svg>
    Data<br>Science
  </div>
  <div class="feature" style="left:268px">
    <svg viewBox="0 0 30 30" fill="none" stroke="#1b3563" stroke-width="1.2"><circle cx="23" cy="6" r="4"/><path d="M4 26c0-7 3-11 7-11s7 4 7 11z"/><rect x="18" y="19" width="9" height="3"/><rect x="18" y="23" width="9" height="3"/></svg>
    Minimize<br>Costs
  </div>
  <a class="btn future-register">Register now</a>
</section>

<section class="prices">
  <h2 class="price-intro-title">Price List</h2>
  <p class="price-intro-text">Let's make the electricity system smarter together</p>
  <p class="price-link">Make a price comparison</p>
  <a class="btn price-compare">Comparison website</a>
  <div class="price-card navy">
    <p class="price-name">Electric<br>Acceleration</p>
    <p class="price-value">6.22</p>
    <p class="price-unit">ISK / kWh</p>
  </div>
  <div class="price-card red">
    <p class="price-name">Electric<br>Acceleration</p>
    <p class="price-value">6.95</p>
    <p class="price-unit">ISK / kWh</p>
  </div>
</section>

<footer class="site-footer">
  <div class="contact" style="left:120px">
    <svg viewBox="0 0 20 24" fill="none" stroke="#fff" stroke-width="1.2"><path d="M10 23C4 15 2 11 2 8a8 8 0 0 1 16 0c0 3-2 7-8 15z"/><circle cx="10" cy="8" r="3"/></svg>
    <div><p class="contact-label">Address</p><p class="contact-value">Ljósavegur 7, 101 Reykjavík</p></div>
  </div>
  <div class="divider" style="left:290px"></div>
  <div class="contact" style="left:313px">
    <svg viewBox="0 0 20 24" fill="none" stroke="#fff" stroke-width="1.2"><rect x="1" y="5" width="18" height="13" rx="1"/><path d="M1 6l9 7 9-7M1 18l7-6M19 18l-7-6"/></svg>
    <div><p class="contact-label">Email address</p><p class="contact-value">hallo@kveldbra.is</p></div>
  </div>
  <div class="divider" style="left:463px"></div>
  <div class="contact" style="left:494px">
    <svg viewBox="0 0 20 24" fill="none" stroke="#fff" stroke-width="1.2"><rect x="1" y="2" width="18" height="20" rx="4"/><path d="M6 7c0 6 3 9 8 10l1.5-2-2.5-2-1.5 1c-1.5-1-2.5-2-3-3.5l1-1.5-2-2.5z"/></svg>
    <div><p class="contact-label">Phone number</p><p class="contact-value">555-0199</p></div>
  </div>
  <p class="copyright">Copyright © Kveldbrá 2020 All rights reserved</p>
</footer>

</body>
</html>
```